Following list to be designed:

1. A4 Letter Head

Must comprise of:
BRISK HARBOR and its LOGO
Address: No.41, 2F, Telvin Court, Marlow Lane, Upper Fennel Gardens, Bangalore 560 078
Tel: 080 41927380
Fax: 080 41927381
Mail: hello@briskharbor.example

Color of wordings to be in the lighter shade of blue and brighter shade of blue.

2. A4 Envelope

Must comprise of:
BRISK HARBOR and its LOGO
Tel: 080 41927380
Fax: 080 41927381

3. Postal Envelope

Must comprise of:
BRISK HARBOR and its LOGO
Tel: 080 41927380
Fax: 080 41927381

4. Business Card

Must comprise of:
Ravi Menon
Managing Partner
Cell: +91 9847162053
Mail: ravimenon@briskharbor.example
Tel: 080 41927380
Fax: 080 41927381

5. A4 Letter Head

Must comprise of:
BRISK HARBOR CORP. (wording) and BRISK HARBOR LOGO (only blue ribbon)

Blue ribbon (BRISK HARBOR LOGO) may be placed on Left Top Corner of the A4 Letter Head
and BRISK HARBOR CORP. (wording) to be placed on Right Top Corner of the A4 Letter Head

Tel: 080 41927380
Fax: 080 41927381

6. . A4 Envelope

Must comprise of:

Blue ribbon (BRISK HARBOR LOGO) may be placed on Left Top Corner of the A4 Envelope
and BRISK HARBOR CORP. (wording) to be placed on Right Top Corner of the A4 Envelope
Tel: 080 41927380
Fax: 080 41927381

Target Market(s)

Top IT/ITES Organizations

Industry/Entity Type

Real Estate Development

Font styles to use
Serif
Sans Serif

Colors
33a6d7
0792cd
85cae6

Requirements
Should not have
• Playful font and color

```html
<!DOCTYPE html>
<html lang="en">
<head>
<meta charset="utf-8">
<title>Brisk Harbor – A4 Letterhead</title>
<link rel="stylesheet" href="https://fonts.googleapis.com/css2?family=PT+Sans+Narrow:wght@400;700&display=swap">
<style>
  :root {
    --backdrop: #8cc3e3;
    --sheet-light: #5ec0e6;
    --sheet-mid: #4a92c4;
    --sheet-dark: #3d6898;
    --band: #3f70a2;
    --band-line: #33a6d7;
    --accent-bright: #0792cd;
    --accent-light: #85cae6;
    --ink-light: #ffffff;
  }
  * { box-sizing: border-box; margin: 0; padding: 0; }
  html, body { width: 1200px; height: 784px; overflow: hidden; }
  body {
    background: var(--backdrop);
    font-family: "PT Sans Narrow", sans-serif;
    display: flex;
    align-items: center;
    justify-content: center;
  }
  .letterhead {
    position: relative;
    width: 509px;
    height: 720px;
    background: linear-gradient(160deg, var(--sheet-light) 0%, var(--sheet-mid) 45%, var(--sheet-dark) 100%);
    box-shadow: 0 6px 18px rgba(30, 70, 110, 0.25);
    overflow: hidden;
  }
  .header-band {
    position: absolute;
    top: 0; left: 0; right: 0;
    height: 44px;
    background: var(--band);
    border-bottom: 3px solid var(--band-line);
  }
  .brand {
    position: absolute;
    top: 0; left: 20px;
    height: 44px;
    display: flex;
    align-items: center;
    gap: 12px;
  }
  .brand-mark {
    width: 28px; height: 28px;
    border-radius: 50%;
    background: var(--accent-light);
  }
  .brand-name {
    font-size: 22px;
    font-weight: 400;
    letter-spacing: 1px;
    color: var(--ink-light);
  }
  .brand-tagline {
    position: absolute;
    top: 16px; right: 24px;
    font-size: 10px;
    letter-spacing: 4px;
    color: var(--accent-light);
  }
  .texture {
    position: absolute;
    background: linear-gradient(135deg, rgba(133, 202, 230, 0.25), rgba(133, 202, 230, 0));
  }
  .texture--top { top: 47px; left: 0; width: 150px; height: 80px; }
  .texture--bottom { bottom: 30px; right: 0; width: 190px; height: 110px;
    background: linear-gradient(315deg, rgba(133, 202, 230, 0.3), rgba(133, 202, 230, 0)); }
  .footer {
    position: absolute;
    left: 0; right: 0; bottom: 0;
    height: 30px;
    padding: 0 14px;
    border-top: 2px solid var(--accent-bright);
    display: flex;
    align-items: center;
    justify-content: center;
    gap: 3px;
    font-size: 8px;
    color: var(--ink-light);
    white-space: nowrap;
  }
  .footer svg { width: 8px; height: 8px; flex: none; }
  .footer .sep { width: 4px; flex: none; }
</style>
</head>
<body>
  <main class="letterhead">
    <div class="header-band"></div>
    <div class="brand">
      <span class="brand-mark"></span>
      <span class="brand-name">BRISK HARBOR</span>
    </div>
    <span class="brand-tagline">ASSET MANAGEMENT</span>

    <div class="texture texture--top" role="img" aria-label="Soft tiled square texture"></div>
    <div class="texture texture--bottom" role="img" aria-label="Soft tiled square texture"></div>

    <footer class="footer">
      <svg viewBox="0 0 10 10" aria-hidden="true"><circle cx="5" cy="5" r="4.5" fill="none" stroke="#fff"/><circle cx="5" cy="4.3" r="1.4" fill="#fff"/></svg>
      <span>No.41, 2F, Telvin Court, Marlow Lane, Upper Fennel Gardens, Bangalore 560 078</span>
      <span class="sep"></span>
      <svg viewBox="0 0 10 10" aria-hidden="true"><circle cx="5" cy="5" r="4.5" fill="none" stroke="#fff"/><path d="M3.3 3h1l.5 1.2-.6.5a3 3 0 0 0 1.2 1.2l.5-.6L7 5.8v1c-2 .2-3.9-1.7-3.7-3.8z" fill="#fff"/></svg>
      <span>080 41927380</span>
      <span class="sep"></span>
      <svg viewBox="0 0 10 10" aria-hidden="true"><circle cx="5" cy="5" r="4.5" fill="none" stroke="#fff"/><rect x="3" y="4" width="4" height="3" fill="#fff"/><rect x="3.7" y="2.7" width="2.6" height="1.3" fill="#fff"/></svg>
      <span>080 41927381</span>
      <span class="sep"></span>
      <svg viewBox="0 0 10 10" aria-hidden="true"><circle cx="5" cy="5" r="4.5" fill="none" stroke="#fff"/><rect x="2.8" y="3.5" width="4.4" height="3" fill="none" stroke="#fff" stroke-width=".8"/><path d="M2.8 3.5 5 5.3l2.2-1.8" fill="none" stroke="#fff" stroke-width=".8"/></svg>
      <span>hello@briskharbor.example</span>
    </footer>
  </main>
</body>
</html>
```